Label Design for honey from a small farm in Italy

We need a label for our Acacia's honey .
We are a little farm in Italy and we would like something like organic, raw and simple.
Maybe with botanical drawing with different color like watercolor o something like that (very important natural and easy)
the jar for 1kg of honey: Capacity: 780 ml - Height: 137 mm - Diameter: ∅ 94 mm
- size approx h 5,5 x 10/14cm ( we use the same label for kg and 500 gr jar)

Industry/Entity Type

Farm

Requirements
Must have
• the writings:
- Acacia
- Miele italiano di Acacia
- Da consumarsi preferibilmente entro: ( and below the space to put the date by the hands)
- some space to put some presentation of the farm or some phrases
- our logo
- the space to put the weight by the hands
- Prodotto da Azienda Agricola ...(produced by Farm Name and address....)
- Confezionato presso Apicoltura... (packaged at apiculture Name and address..)
- graphic of Acacia’s flowers ( like drawing)
Should not have
• Barcode
nutritional table

```html
<!DOCTYPE html>
<html lang="it">
<head>
<meta charset="utf-8">
<title>Acacia – Miele italiano di Acacia</title>
<link rel="stylesheet" href="https://fonts.googleapis.com/css2?family=Arimo:wght@700&family=Marcellus&family=PT+Sans+Narrow&family=PT+Serif&display=swap">
<style>
  :root {
    --page: #ffffff;
    --frame: #8f8a60;
    --mustard: #cf9a2c;
    --plum: #7b1a4c;
    --plum-edge: #a65a84;
    --cream: #f3e4c2;
    --field: #e7c98e;
    --field-text: #c49a4c;
    --ink: #2a1f10;
    --leaf: #bfe0d4;
    --bloom: #f2d54a;
  }
  html, body {
    margin: 0;
    width: 893px;
    height: 1200px;
    overflow: hidden;
    background: var(--page);
  }
  .label {
    position: absolute;
    left: 20px;
    top: 390px;
    width: 853px;
    height: 420px;
    display: block;
  }
  .frame { fill: var(--frame); }
  .info-panel { fill: var(--mustard); }
  .badge { fill: var(--plum); stroke: var(--plum-edge); stroke-width: 6; }
  .ribbon { fill: var(--plum); stroke: var(--plum-edge); stroke-width: 3; }
  .farm-name {
    font-family: "PT Sans Narrow", sans-serif;
    font-size: 24px;
    fill: var(--cream);
    letter-spacing: 1px;
  }
  .variety {
    font-family: "Arimo", sans-serif;
    font-weight: 700;
    font-size: 54px;
    fill: #ffffff;
  }
  .subtitle {
    font-family: "Marcellus", serif;
    font-size: 21px;
    fill: var(--cream);
  }
  .note-outline { fill: none; stroke: #e2bb62; stroke-width: 2; }
  .note {
    font-family: "PT Serif", serif;
    font-size: 13px;
    fill: var(--ink);
  }
  .info {
    font-family: "PT Sans Narrow", sans-serif;
    font-size: 18px;
    fill: var(--ink);
  }
  .write-in { fill: var(--field); }
  .write-in-hint {
    font-family: "PT Sans Narrow", sans-serif;
    font-size: 17px;
    fill: var(--field-text);
  }
</style>
</head>
<body>
<svg class="label" viewBox="0 0 853 420" xmlns="http://www.w3.org/2000/svg">
  <defs>
    <linearGradient id="botanical-tone" x1="0" y1="0" x2="1" y2="1">
      <stop offset="0" stop-color="#f7fbf6"/>
      <stop offset="0.45" stop-color="var(--leaf)"/>
      <stop offset="0.7" stop-color="#f7efc0"/>
      <stop offset="1" stop-color="var(--bloom)"/>
    </linearGradient>
  </defs>

  <rect class="frame" x="0" y="0" width="853" height="420"/>
  <rect class="botanical" x="8" y="8" width="370" height="404" fill="url(#botanical-tone)"
        role="img" aria-label="Watercolour drawing of acacia branches with yellow blossoms"/>
  <rect class="info-panel" x="378" y="8" width="467" height="404"/>

  <!-- variety badge -->
  <polygon class="badge" points="55,215 115,92 265,92 325,215 265,337 115,337"/>
  <text class="farm-name" x="190" y="160" text-anchor="middle">IL FIENILE</text>
  <text class="variety" x="190" y="236" text-anchor="middle">Acacia</text>
  <polygon class="ribbon" points="62,276 78,254 302,254 318,276 302,298 78,298"/>
  <text class="subtitle" x="190" y="284" text-anchor="middle">Miele italiano di Acacia</text>

  <!-- presentation space -->
  <path class="note-outline" d="M352 150 L382 222 L482 222 L520 150"/>
  <g transform="translate(372 168) rotate(-30)">
    <text class="note" x="0" y="0">space to put some</text>
    <text class="note" x="6" y="16">presentation</text>
    <text class="note" x="12" y="32">of the farm or some phrases</text>
  </g>

  <!-- write-in fields -->
  <text class="info" x="532" y="146">Da consumarsi preferibilmente entro</text>
  <polygon class="write-in" points="545,162 795,162 810,185 795,210 545,210 558,185"/>
  <polygon class="write-in" points="545,220 795,220 810,244 795,268 545,268 558,244"/>
  <text class="write-in-hint" x="680" y="250" text-anchor="middle">weight</text>

  <!-- producer details -->
  <text class="info" x="665" y="322" text-anchor="middle">Prodotto da Azienda Agricola</text>
  <text class="info" x="665" y="346" text-anchor="middle">...(produced by Farm Name and address....)</text>
  <text class="info" x="665" y="374" text-anchor="middle">Confezionato presso Apicoltura</text>
  <text class="info" x="665" y="398" text-anchor="middle">... (packaged at apiculture Name and address..)</text>
</svg>
</body>
</html>
```